Waterless soap seeking funky new design

We are looking for a talented designer to create a fresh and appealing label design for one of our current products. We do have a current logo that we really like and use in several places. We would like the new label design to work with and incorporate the current logo.
The product is our Grit Bloom wipe-off soap. It is made by hand, in small batches. We would like the label design to reflect the hand made aspect of the product. We are not requiring the label to be illustrated but we do like the hand drawn and hand made tie. and the illustration does appeal to us.
Please see the attached current logo that we do like. you can see it used in the attached current label, that we DONT like. this is what we are seeking, a new label for our Grit Bloom soap.
The soap is made for real messes, grease, grime and busted knuckles. It is made using natural ingredients. this is not a Men Only product, it is definitely geared toward men and would like the label to reflect that.

Target Market(s)

Mechanics, tradesmen, welders, People who get dirty for a living

Colors
0054AA
0677BA
7BADD7
CADEEF
E8F1F8
EE7325
F08F49
F5BC92
FAE3D3
FDF4ED
EB3D1F
EC4F4E
F09395
F8D3D4
FCEDEE

Requirements
Must have
• Keep the current logo. It can play a smaller role in the label, but we do use this logo else were in other promo items, and we don't want it to be completely gone.
Nice to have
• I would like to have something illustrated, I am not sold on this but I like the idea of a hand drawn(or at least in part) label to tie into the 'hand made' aspect
Should not have
• Current Font styles, We are currently selling product but we don't care for our font styles.

```html
<!DOCTYPE html>
<html lang="en">
<head>
<meta charset="utf-8">
<title>Grit Bloom Wipeoff Soap Label</title>
<link rel="stylesheet" href="https://fonts.googleapis.com/css2?family=Black+Ops+One&family=Bebas+Neue&display=swap">
<style>
  :root {
    --backdrop: #efe9e3;
    --kraft: #c6b197;
    --kraft-shade: #b9a386;
    --ink: #1f1d1b;
  }
  * { margin: 0; padding: 0; box-sizing: border-box; }
  html, body { width: 1200px; height: 596px; overflow: hidden; }
  body {
    background: var(--backdrop);
    display: flex;
    justify-content: center;
    align-items: center;
  }
  .label {
    position: relative;
    width: 307px;
    height: 596px;
    background: radial-gradient(circle at 40% 30%, var(--kraft) 0%, var(--kraft-shade) 100%);
    color: var(--ink);
    font-family: "Bebas Neue", sans-serif;
  }
  .brand {
    position: absolute;
    top: 25px;
    left: 0;
    width: 100%;
    height: 126px;
    display: flex;
    justify-content: center;
    align-items: center;
  }
  .brand-name {
    font-size: 30px;
    letter-spacing: 2px;
    line-height: 1;
    color: var(--ink);
  }
  .headline {
    position: absolute;
    top: 188px;
    left: 28px;
    width: 250px;
    height: 172px;
  }
  .headline text { fill: var(--ink); }
  .headline .title-line { font-family: "Black Ops One", sans-serif; }
  .headline .sub-line { font-family: "Bebas Neue", sans-serif; }
  .craft-badge {
    position: absolute;
    top: 397px;
    left: 123px;
    width: 60px;
    height: 60px;
  }
  .claims {
    position: absolute;
    top: 489px;
    left: 0;
    width: 100%;
    text-align: center;
    font-size: 19px;
    line-height: 23px;
    letter-spacing: 0.5px;
  }
  .footer {
    position: absolute;
    bottom: 14px;
    left: 24px;
    right: 22px;
    display: flex;
    justify-content: space-between;
    font-size: 14px;
    letter-spacing: 0.5px;
  }
</style>
</head>
<body>
  <main class="label">
    <header class="brand">
      <span class="brand-name">Ironhand Soap Co.</span>
    </header>

    <svg class="headline" viewBox="0 0 250 172" aria-label="Grit Bloom Wipeoff Soap">
      <text class="title-line" x="0" y="54" font-size="56" textLength="248" lengthAdjust="spacingAndGlyphs">GRIT</text>
      <text class="title-line" x="0" y="124" font-size="64" textLength="248" lengthAdjust="spacingAndGlyphs">BLOOM</text>
      <text class="sub-line" x="2" y="170" font-size="46" textLength="244" lengthAdjust="spacingAndGlyphs">WIPEOFF SOAP</text>
    </svg>

    <svg class="craft-badge" viewBox="0 0 60 60" role="img" aria-label="Handmade small batch badge">
      <circle cx="30" cy="30" r="28" fill="none" stroke="var(--ink)" stroke-width="3"/>
      <circle cx="30" cy="30" r="16" fill="var(--ink)"/>
    </svg>

    <p class="claims">Eczema Friendly<br>All Natural Ingredients</p>

    <footer class="footer">
      <span class="net-weight">12oz</span>
      <span class="origin">Made in USA</span>
    </footer>
  </main>
</body>
</html>
```